Flyer-Design für Energy-Drink
Zielgruppe
Es geht um einen neuen, gesunden Energy-Drink
Aufgabenstellung
Der Flyer sollte A5 entweder vorne und hinten bedruckt und ungefaltet sein
oder
A5 gefaltet auf A6 sein
Er soll junge Menschen ansprechen und hipp sein
Er soll erwachsene Menschen jeden Alters mit einem Gesundheitsbewusstsein ansprechen
Wichtig ist: kein Zuckerzusatz - 50% Fruchtanteil - ohne Chemie - absolut natürlich
wertvolle Vital und Inhaltsstoffe
einzigartiger, fruchtiger Geschmack, wenig Kohlensäure
gekühlt und geschüttelt trinken
Kick vor dem Sport oder einfach zwischendurch.
Neuer Antrieb
anregend, belebend
Dose ist zu 100% recycelbar

```html
<!DOCTYPE html>
<html lang="de">
<head>
<meta charset="utf-8">
<title>Vivant Energy-Drink Flyer</title>
<link href="https://fonts.googleapis.com/css2?family=Montserrat:ital,wght@0,500;0,600;0,700;0,900;1,800&display=swap" rel="stylesheet">
<style>
  :root {
    --page-bg: #8e8e8e;
    --red-deep: #8f0d10;
    --red: #c1141a;
    --red-bright: #e3261c;
    --orange: #f28a1c;
    --yellow-glow: #ffc21a;
    --yellow: #e6c52a;
    --yellow-text: #f0d21e;
    --can-dark: #1c1b1c;
    --can-mid: #3a2a2c;
    --band-dark: #1e1e20;
    --band-stripe: #3a3a3d;
    --ice: #9fb6c4;
    --white: #ffffff;
    --imprint: #7a0b0e;
  }
  * { margin: 0; padding: 0; box-sizing: border-box; }
  html, body { width: 1200px; height: 1200px; overflow: hidden; }
  body {
    background: var(--page-bg);
    font-family: "Montserrat", Arial, sans-serif;
    position: relative;
  }
  .flyer {
    position: absolute;
    top: 205px;
    width: 560px; height: 790px;
    overflow: hidden;
    color: var(--white);
    box-shadow: 0 8px 24px rgba(0,0,0,.3);
  }
  .flyer--front { left: 30px; background: var(--red); }
  .flyer--back { left: 610px; background: var(--red); }

  /* Front */
  .front__art {
    position: absolute; inset: 0;
    background:
      radial-gradient(circle at 55% 45%, var(--red) 0 9%, var(--yellow-glow) 15%, var(--orange) 24%, var(--red-bright) 34%, var(--orange) 42%, var(--red) 56%, var(--red-deep) 100%);
  }
  .intro {
    position: absolute;
    top: 44px; left: 40px; right: 40px;
    text-align: center;
    font-weight: 600;
    font-size: 17.5px;
    line-height: 1.3;
    letter-spacing: 0.3px;
  }
  .intro p + p { margin-top: 18px; }
  .imprint {
    position: absolute;
    left: 34px; top: 640px;
    transform-origin: left top;
    transform: rotate(-90deg);
    white-space: nowrap;
    font-size: 14px;
    font-weight: 500;
    color: var(--imprint);
  }
  .can {
    position: absolute;
    left: 90px; top: 240px;
    width: 190px; height: 440px;
    border-radius: 20px 20px 26px 26px;
    background: linear-gradient(90deg, var(--can-dark) 0%, var(--can-mid) 35%, #6b1d1f 50%, var(--can-mid) 65%, var(--can-dark) 100%);
    transform: rotate(8deg);
    box-shadow: 0 14px 22px rgba(0,0,0,.35);
  }
  .slogan {
    position: absolute;
    left: 300px; top: 500px;
    width: 240px;
    text-align: right;
    font-weight: 800;
    font-style: italic;
    font-size: 40px;
    line-height: 1.02;
    letter-spacing: -1px;
    text-shadow: 2px 2px 3px rgba(0,0,0,.35);
  }
  .recycle {
    position: absolute;
    left: 34px; bottom: 30px;
    font-size: 16px; font-weight: 600; line-height: 1.25;
    text-align: center;
  }
  .order {
    position: absolute;
    left: 148px; bottom: 32px;
    font-size: 16px; font-weight: 600; line-height: 1.3;
    color: var(--yellow-text);
    text-align: right;
    white-space: nowrap;
  }
  .partner-box {
    position: absolute;
    right: 18px; bottom: 30px;
    width: 196px; height: 80px;
    border-radius: 8px;
    background: var(--yellow);
  }

  /* Back */
  .back__band {
    position: absolute; left: 0; right: 0; top: 0; height: 150px;
    background: repeating-linear-gradient(-60deg, var(--band-dark) 0 22px, var(--band-stripe) 22px 44px);
  }
  .back__glow {
    position: absolute; left: 0; right: 0; top: 120px; bottom: 0;
    background: radial-gradient(ellipse at 50% 40%, var(--red-bright) 0%, var(--red) 45%, var(--red-deep) 100%);
  }
  .headline {
    position: absolute;
    left: 0; right: 0; top: 28px;
    text-align: center;
    font-weight: 900;
    font-size: 84px;
    line-height: 1.02;
    letter-spacing: -2px;
    text-transform: uppercase;
  }
  .benefits {
    position: absolute;
    left: 48px; top: 390px;
    list-style: none;
    font-weight: 700;
    font-size: 22px;
    line-height: 1.22;
    letter-spacing: -0.5px;
  }
  .ice {
    position: absolute; left: 0; right: 0; bottom: 0; height: 210px;
    background: linear-gradient(180deg, var(--band-dark) 0%, #3c4a54 40%, var(--ice) 100%);
    clip-path: polygon(0 30%, 50% 8%, 100% 0, 100% 100%, 0 100%);
  }
</style>
</head>
<body>
  <article class="flyer flyer--front">
    <div class="front__art" role="img" aria-label="Tanzende Silhouetten vor leuchtend orange-gelben Kreisringen auf rotem Grund"></div>
    <div class="intro">
      <p>Der neue fruchtige Vivant Energy-Drink steigert deine Leistung immer dann, wenn es darauf ankommt. Egal ob vor dem Sport, bei einem Durchhänger im Job oder einfach als erfrischender Kick.</p>
      <p>Vivant aktiviert und treibt dich wieder neu an.</p>
    </div>
    <div class="imprint">Vitalwerk24 GmbH - Lindenweg 12 - 4600 Musterlingen</div>
    <div class="can" role="img" aria-label="Dunkle Getränkedose mit Wassertropfen"></div>
    <p class="slogan">kühlen,<br>schütteln,<br>geniessen!</p>
    <p class="recycle">Dose 100%<br>recyclebar</p>
    <p class="order">bestellbar bei Ihrem<br>Vitalwerk24 Partner:</p>
    <div class="partner-box"></div>
  </article>

  <article class="flyer flyer--back">
    <div class="back__band"></div>
    <div class="back__glow"></div>
    <h1 class="headline">Vivant<br>Your<br>Energy</h1>
    <ul class="benefits">
      <li>kein Zuckerzusatz</li>
      <li>keine Chemie</li>
      <li>wertvolle Vital- und</li>
      <li>Inhaltsstoffe</li>
      <li>50% Fruchtanteil</li>
      <li>anregend, belebend</li>
      <li>wenig Kohlensäure</li>
    </ul>
    <div class="ice" role="img" aria-label="Eiswürfel und Getränkedose auf dunklem Grund"></div>
  </article>
</body>
</html>
```